creating professional text layers for Bramwell Product listings images

I need some text added to several images in a professional eye catching way. The text should be legible on desktop and mobile devices. Rough mocks will be provided. You will just need to make them pop and professional. There are 10 images required in total to the selected designer. Below are just 3 of them

```html
<!DOCTYPE html>
<html lang="en">
<head>
<meta charset="utf-8">
<title>Bramwell Listing Images – Wire Stripper Text Layers</title>
<link rel="stylesheet" href="https://fonts.googleapis.com/css2?family=Jost:wght@700;800&family=Montserrat:wght@800&display=swap">
<style>
  :root {
    --board-light: #cfe0f2;
    --board-dark: #0a1640;
    --brand-blue: rgba(8, 44, 170, 0.9);
    --brand-blue-side: rgba(10, 36, 150, 0.82);
    --accent-yellow: #f6e71c;
    --text-white: #ffffff;
    --photo-workshop-a: #5b6470;
    --photo-workshop-b: #2b3140;
    --photo-studio-a: #1a1a1d;
    --photo-studio-b: #b88c5e;
  }
  * { box-sizing: border-box; margin: 0; padding: 0; }
  html, body { width: 1177px; height: 1200px; overflow: hidden; }
  body { position: relative; background: var(--board-dark); }

  .board-backdrop { position: absolute; inset: 0; width: 1177px; height: 1200px; }

  .listing-tile {
    position: absolute;
    width: 507px;
    height: 508px;
    overflow: hidden;
    box-shadow: 0 10px 28px rgba(0, 0, 20, 0.45);
  }
  .tile-a { left: 56px; top: 62px; }
  .tile-b { left: 612px; top: 62px; }
  .tile-c { left: 55px; top: 630px; }
  .tile-d { left: 612px; top: 630px; }

  .product-photo { position: absolute; inset: 0; }
  .photo-workshop {
    background:
      radial-gradient(ellipse at 30% 45%, #d9d4bf 0%, rgba(217,212,191,0) 38%),
      radial-gradient(ellipse at 78% 65%, #8f949b 0%, rgba(143,148,155,0) 40%),
      linear-gradient(160deg, var(--photo-workshop-a), var(--photo-workshop-b));
  }
  .photo-studio {
    background:
      radial-gradient(ellipse at 22% 45%, #e6e0cf 0%, rgba(230,224,207,0) 40%),
      linear-gradient(180deg, var(--photo-studio-a) 0%, var(--photo-studio-a) 34%, var(--photo-studio-b) 36%, #d3a878 100%);
  }
  .photo-bench {
    background:
      radial-gradient(ellipse at 72% 45%, #a7adb6 0%, rgba(167,173,182,0) 42%),
      linear-gradient(180deg, #2a3140 0%, #3a404c 68%, #d8b98e 72%, #e4c79d 100%);
  }

  .color-overlay { position: absolute; inset: 0; width: 100%; height: 100%; }

  .headline {
    position: absolute;
    font-family: "Jost", sans-serif;
    font-weight: 800;
    text-transform: uppercase;
    letter-spacing: -2.5px;
    color: var(--text-white);
  }
  .headline span { display: block; }
  .headline .accent { color: var(--accent-yellow); }

  .headline-feature {
    font-size: 52px;
    line-height: 39px;
  }
  .tile-a .headline-feature { left: 257px; top: 30px; }
  .tile-c .headline-feature { left: 263px; top: 22px; }
  .tile-d .headline-feature { left: 259px; top: 31px; }

  .headline-value {
    left: 40px;
    top: 112px;
    font-size: 80px;
    line-height: 65px;
    letter-spacing: -3px;
  }

  .question {
    position: absolute;
    font-family: "Montserrat", sans-serif;
    font-weight: 800;
    font-size: 20.5px;
    line-height: 21.5px;
    text-transform: uppercase;
    color: var(--text-white);
    letter-spacing: -0.2px;
  }
  .question .accent { color: var(--accent-yellow); }
  .tile-a .question { left: 92px; top: 413px; }
  .tile-c .question { left: 98px; top: 410px; }
  .tile-d .question { left: 92px; top: 413px; }
</style>
</head>
<body>

<svg class="board-backdrop" viewBox="0 0 1177 1200" aria-hidden="true">
  <rect width="1177" height="1200" fill="var(--board-dark)"/>
  <polygon points="0,0 537,0 195,1200 0,1200" fill="var(--board-light)"/>
</svg>

<section class="listing-tile tile-a">
  <div class="product-photo photo-workshop" role="img" aria-label="Close-up of the wire stripping machine's control box with speed dial, emergency stop and power switch, in a workshop"></div>
  <svg class="color-overlay" viewBox="0 0 507 508" preserveAspectRatio="none" aria-hidden="true">
    <polygon points="0,392 507,357 507,508 0,508" fill="var(--brand-blue)"/>
  </svg>
  <h2 class="headline headline-feature"><span>Variable</span><span class="accent">Speed</span><span>Control</span></h2>
  <p class="question">How could you possibly<br>strip <span class="accent">all gauges at the<br>same speed?</span></p>
</section>

<section class="listing-tile tile-b">
  <div class="product-photo photo-bench" role="img" aria-label="Person standing behind the wire stripping machine on a wooden workbench with scrap wire"></div>
  <svg class="color-overlay" viewBox="0 0 507 508" preserveAspectRatio="none" aria-hidden="true">
    <polygon points="0,0 195,0 160,508 0,508" fill="var(--brand-blue-side)"/>
  </svg>
  <h2 class="headline headline-value"><span class="accent">Pays</span><span class="accent">For</span><span class="accent">Itself</span><span>Fast</span></h2>
</section>

<section class="listing-tile tile-c">
  <div class="product-photo photo-studio" role="img" aria-label="Angled view of the wire stripping machine with control box and hand wheel on a wooden table"></div>
  <svg class="color-overlay" viewBox="0 0 507 508" preserveAspectRatio="none" aria-hidden="true">
    <polygon points="0,392 507,357 507,508 0,508" fill="var(--brand-blue)"/>
  </svg>
  <h2 class="headline headline-feature"><span>Variable</span><span class="accent">Speed</span><span>Control</span></h2>
  <p class="question">How could you possibly<br>strip <span class="accent">all gauges at the<br>same speed?</span></p>
</section>

<section class="listing-tile tile-d">
  <div class="product-photo photo-workshop" role="img" aria-label="Close-up of the wire stripping machine's control box with speed dial, emergency stop and power switch, in a workshop"></div>
  <svg class="color-overlay" viewBox="0 0 507 508" preserveAspectRatio="none" aria-hidden="true">
    <polygon points="0,392 507,357 507,508 0,508" fill="var(--brand-blue)"/>
  </svg>
  <h2 class="headline headline-feature"><span>Variable</span><span class="accent">Speed</span><span>Control</span></h2>
  <p class="question">How could you possibly<br>strip <span class="accent">all gauges at the<br>same speed?</span></p>
</section>

</body>
</html>
```